Webdesign für Vernetzung christlicher Geschäftsleute
Zielgruppe
Die Vereinigung KRTWLE bezweckt die Vernetzung christlicher Geschäftsleute und die Verbreitung von Biblisch fundierten ethischen Geschäftsprinzipien. Die Zielgruppe umfasst Unternehmer und Verantwortungsträger aus Wirtschaft und Politik.
Aufgabenstellung
Ich suche einen Designer, welcher sich ernsthaft mit den Anforderungen und dem Design auseinandersetzt und eine Individuelle Lösung gestaltet.
Das Logo sowie ein unverbindlicher Vorschlag für die Strukturierung liegen bei.
Bitte keine 08/15 Business Stock Fotos (Händeschütteln, Meetings, Präsentationen).
Das Design soll folgende Seiten beinhalten (Beschreibung folgt):
- Startseite
- Standardseite (Titel, Text mit Bildern)
- Event-Detail Seite (Titel, Ort, Datum, ev. Foto, Beschreibungstext, ev. Map)
- Chapter Startseite
Die bestehende Webseite ist kein Massstab ;).

```html
<!DOCTYPE html>
<html lang="de">
<head>
<meta charset="utf-8">
<title>KRTWLE – Start</title>
<link rel="stylesheet" href="https://fonts.googleapis.com/css2?family=Open+Sans:wght@400;600;700&family=Cinzel:wght@700&display=swap">
<style>
  :root {
    --red: #a50f2d;
    --ink: #111111;
    --text: #2a2a2a;
    --white: #ffffff;
    --band: #eae9ea;
    --tile: #f3f3f4;
    --numeral: #5a5a5c;
  }
  html, body {
    margin: 0; padding: 0;
    width: 1200px; height: 613px; overflow: hidden;
  }
  body {
    background: var(--band);
    font-family: "Open Sans", Arial, sans-serif;
    color: var(--ink);
  }
  .page {
    position: relative; width: 1200px; height: 613px; overflow: hidden;
    background: var(--band);
  }
  .header-band {
    position: absolute; left: 0; top: 0; width: 1200px; height: 420px;
    background: var(--white);
  }
  .brand {
    position: absolute; left: 150px; top: 55px;
    display: flex; align-items: center; gap: 8px;
  }
  .brand-dot {
    width: 18px; height: 18px; border-radius: 50%; background: var(--red);
  }
  .brand-name {
    font-weight: 700; font-size: 22px; line-height: 26px; color: var(--red); letter-spacing: 1px;
  }
  .main-nav {
    position: absolute; top: 58px; left: 0; width: 1200px; height: 30px;
  }
  .main-nav a {
    position: absolute; top: 0; font-weight: 600; font-size: 15px; line-height: 20px;
    color: var(--ink); text-decoration: none; letter-spacing: 0.3px;
  }
  .main-nav a.active::after {
    content: ""; position: absolute; left: -4px; right: -4px; bottom: -6px;
    height: 3px; background: var(--red);
  }
  .hero-image {
    position: absolute; left: 302px; top: 128px; width: 706px; height: 354px;
    background:
      radial-gradient(ellipse 60% 45% at 40% 55%, #8a8a8e 0%, #bdbdc0 45%, rgba(230,230,232,0) 80%),
      linear-gradient(180deg, #d6d4d8 0%, #f1f0f1 35%, #e4e3e5 70%, #f7f6f7 100%);
    box-shadow: 0 6px 18px rgba(0,0,0,0.12);
  }
  .chapter-toggle {
    position: absolute; left: 881px; top: 145px;
    display: flex; align-items: center; gap: 14px;
    font-weight: 600; font-size: 14px; line-height: 19px; color: var(--ink);
  }
  .hero-title {
    position: absolute; left: 196px; top: 198px; margin: 0;
    font-weight: 700; font-size: 39px; line-height: 49px; letter-spacing: 0.5px;
  }
  .hero-title span {
    display: inline-block; background: var(--white); padding: 0 10px 0 11px;
  }
  .section-title {
    position: absolute; top: 505px; margin: 0;
    font-weight: 700; font-size: 25px; line-height: 34px; color: var(--red); letter-spacing: 0.3px;
  }
  .welcome-text {
    position: absolute; left: 161px; top: 558px; width: 490px; margin: 0;
    font-size: 12.5px; line-height: 18px; color: var(--text);
  }
  .chapter-tile {
    position: absolute; top: 549px; width: 134px; height: 64px;
    background: linear-gradient(160deg, #fafafa, var(--tile));
    box-shadow: 0 2px 8px rgba(0,0,0,0.08);
    text-align: center; overflow: hidden;
    font-family: "Cinzel", Georgia, serif; font-weight: 700;
    font-size: 46px; line-height: 90px; color: var(--numeral);
  }
</style>
</head>
<body>
<div class="page">
  <div class="header-band"></div>

  <div class="brand">
    <div class="brand-dot"></div>
    <div class="brand-name">KRTWLE</div>
  </div>

  <nav class="main-nav">
    <a href="#" class="active" style="left:624px;">START</a>
    <a href="#" style="left:743px;">ÜBER UNS</a>
    <a href="#" style="left:903px;">KONTAKT</a>
  </nav>

  <div class="hero-image" role="img" aria-label="Schneebedeckter Berggipfel in Wolken"></div>

  <div class="chapter-toggle">
    <span>CHAPTER</span>
    <svg width="23" height="19" viewBox="0 0 23 19" aria-hidden="true">
      <rect x="0" y="0" width="23" height="3.5" fill="#111"/>
      <rect x="0" y="7.5" width="23" height="3.5" fill="#111"/>
      <rect x="0" y="15" width="23" height="3.5" fill="#111"/>
    </svg>
  </div>

  <h1 class="hero-title">
    <span>SEIN</span><br>
    <span>ZEICHEN</span><br>
    <span>ÜBER UNS</span><br>
    <span>IST LIEBE</span>
  </h1>

  <h2 class="section-title" style="left:161px;">WILLKOMMEN</h2>
  <p class="welcome-text">Lorem ipsum dolor sit amet, consetetur sadipscing elitr, sed diam nonumy eirmod tempor invidunt ut labore et dolore magna aliquyam erat, sed diam voluptua. Ate vero eos et accusam et justo duo dolores et ea rebum. Stet clita kasd gubergren,</p>

  <h2 class="section-title" style="left:745px;">CHAPTERS</h2>
  <div class="chapter-tile" style="left:745px;">I</div>
  <div class="chapter-tile" style="left:917px;">II</div>
</div>
</body>
</html>
```